Business card-Tales From The Harbor Gate

Looking for a business card. I have a website I designed "TalesFromTheHarborGate.com I am not a graphic artist and may at some point need help with my website too. Used the font "Hello Stockholm" on my website. I am a writer, looking to get published. Liked the "feel" of the cover below. No cliche typwriters, keyboards, pens. - Edgar P. Lindqvist
Updates

Not 100% sold on needing the owls, just a place to begin. I probably sounds like I'm going to be a pain to work with, I was a video production manager for 15+ years. When I would give an editor or graphic artist a project and let them run with it, the results were typically beyond my expectations. I give the idea then as the artists touch it, and adds value I could never bring to the project. Make something you would be proud of, don't try to second-guess me.

Target Market(s)

Agents, publishers, people I want to buy my book once I get it published

Industry/Entity Type

Publishing

Contact Information for Business Card

Edgar P. Lindqvist
TalesFromTheHarborGate.com
Phone #-TBD
Edgar@TalesFromTheHarbroGate.com
Maybe address; 418 N. 7th St Cheyenne, WY 82947

Colors
fcca95
3277b5

Requirements
Must have
• I like the "chromatic" feel of the attached cover. As you can see from my website, I'm an owl fan. Those pictures I took and do own the rights too. Not sure if they are approritae for a business card.
Should not have
• Cliche I like the "chromatic" feel of the attached book cover.
• I will need help with my website at some point too. I want the website to be easy for me to update, and reflect the same feel as the card. I write adventure, mystery. I have romance in my books too...Adventure of Romance, Romance of adventure, I am not sure but those words were like by an author firned of mine. They are rather "light" reading too.

```html
<!DOCTYPE html>
<html lang="en">
<head>
<meta charset="utf-8">
<title>Edgar P. Lindqvist — Business Card</title>
<link href="https://fonts.googleapis.com/css2?family=Bebas+Neue&family=Roboto:wght@300;400&display=swap" rel="stylesheet">
<style>
  :root {
    --page-bg: #3a3430;
    --card-blue: #2a7cc4;
    --card-blue-deep: #2474bd;
    --card-cream: #ece8e2;
    --photo-warm: #c9b59a;
    --photo-brown: #8a7560;
    --photo-grey: #a9b0b8;
    --ink-white: #ffffff;
  }
  html, body {
    margin: 0;
    width: 1200px;
    height: 930px;
    overflow: hidden;
    background: var(--page-bg);
  }
  .stage {
    width: 1200px;
    height: 930px;
    display: flex;
    align-items: center;
    justify-content: center;
  }
  .business-card {
    position: relative;
    width: 1000px;
    height: 572px;
    border-radius: 24px;
    overflow: hidden;
    background: linear-gradient(180deg, var(--card-cream) 0%, #dcdde0 35%, #9fbfdd 58%, var(--card-blue) 78%, var(--card-blue-deep) 100%);
    box-shadow: 0 18px 40px rgba(0,0,0,0.35);
  }
  .owl-photo {
    position: absolute;
    left: 180px;
    top: 0;
    width: 560px;
    height: 470px;
    background:
      radial-gradient(ellipse 38% 42% at 50% 45%, var(--photo-brown) 0%, var(--photo-warm) 45%, rgba(201,181,154,0) 100%),
      radial-gradient(ellipse 30% 40% at 80% 20%, rgba(220,180,170,0.6) 0%, rgba(220,180,170,0) 100%),
      radial-gradient(ellipse 50% 50% at 55% 75%, var(--photo-grey) 0%, rgba(169,176,184,0) 100%);
    -webkit-mask-image: linear-gradient(180deg, #000 0%, #000 55%, transparent 100%);
    mask-image: linear-gradient(180deg, #000 0%, #000 55%, transparent 100%);
  }
  .identity {
    position: absolute;
    left: 70px;
    top: 400px;
    color: var(--ink-white);
    text-align: right;
  }
  .identity-name {
    font-family: "Bebas Neue", sans-serif;
    font-size: 66px;
    line-height: 1;
    letter-spacing: 1px;
    margin: 0;
    font-weight: 400;
  }
  .identity-role {
    font-family: "Roboto", sans-serif;
    font-weight: 300;
    font-size: 24px;
    margin: 2px 0 0;
  }
  .divider {
    position: absolute;
    left: 520px;
    top: 360px;
    width: 2px;
    height: 150px;
    background: var(--ink-white);
  }
  .contact-list {
    position: absolute;
    left: 548px;
    top: 352px;
    margin: 0;
    padding: 0;
    list-style: none;
    color: var(--ink-white);
    font-family: "Roboto", sans-serif;
    font-weight: 300;
    font-size: 23px;
  }
  .contact-item {
    display: flex;
    align-items: center;
    gap: 12px;
    height: 38px;
  }
  .contact-icon {
    width: 18px;
    height: 18px;
    flex: none;
  }
</style>
</head>
<body>
  <main class="stage">
    <section class="business-card">
      <div class="owl-photo" role="img" aria-label="Photograph of a great horned owl looking toward the viewer, fading into blue"></div>

      <div class="identity">
        <h1 class="identity-name">EDGAR P. LINDQVIST</h1>
        <p class="identity-role">Director</p>
      </div>

      <div class="divider"></div>

      <ul class="contact-list">
        <li class="contact-item">
          <svg class="contact-icon" viewBox="0 0 24 24" fill="none" stroke="#fff" stroke-width="2" stroke-linecap="round"><path d="M5 3h4l2 5-3 2a11 11 0 0 0 6 6l2-3 5 2v4a2 2 0 0 1-2 2A17 17 0 0 1 3 5a2 2 0 0 1 2-2z"/></svg>
          <span>+330 5172-4036</span>
        </li>
        <li class="contact-item">
          <svg class="contact-icon" viewBox="0 0 24 24" fill="none" stroke="#fff" stroke-width="2"><rect x="3" y="5" width="18" height="14" rx="1"/><path d="M3 6l9 7 9-7"/></svg>
          <span>Edgar@TalesFromTheHarbroGate.com</span>
        </li>
        <li class="contact-item">
          <svg class="contact-icon" viewBox="0 0 24 24" fill="none" stroke="#fff" stroke-width="2"><circle cx="12" cy="12" r="9"/><path d="M3 12h18M12 3c3 3 3 15 0 18M12 3c-3 3-3 15 0 18"/></svg>
          <span>www.TalesFromTheHarborGate.com</span>
        </li>
        <li class="contact-item">
          <svg class="contact-icon" viewBox="0 0 24 24" fill="#fff"><path d="M12 2a7 7 0 0 0-7 7c0 5 7 13 7 13s7-8 7-13a7 7 0 0 0-7-7zm0 9.5A2.5 2.5 0 1 1 12 6.5a2.5 2.5 0 0 1 0 5z"/></svg>
          <span>418 N. 7th St Cheyenne, WY 82947</span>
        </li>
      </ul>
    </section>
  </main>
</body>
</html>
```